Corporate Design für aufstrebende Immobilienmaklerin
Herr Brandl ist auf alle Wünsche eingegangen und hat meine Erwartungen an den Ablauf des Projektes in vielerlei Hinsicht übertroffen. Auch als es von meiner Seite Verzögerung gab, war er sehr verständnisvoll und hat gewartet, bis alles soweit war. Würde immer wieder mit ihm arbeiten.
Zielgruppe
Ich bin eine junge Immobilienmaklerin, die sich neu am Markt etablieren möchte.
Mein Service für Kunden umfasst das folgende Programm:
Wertermittlung
Marktanalyse
Energieausweis
Vermarktung
z.T. Home Staging
Vorbereitung Kaufverträge
Begleitung zum Notar...
Zielgruppe: Immobilienbesitzer, Käufer, Verkäufer, alle die gerne einen Mehrwert rund um die Immobilie haben möchten
Aufgabenstellung
Ich suche ein Design für meine Geschäftsunterlagen. Der Betrachter soll ein gutes Gefühl bekommen. Es soll seriös, edel und dynamisch wirken. Aber vor allem auch vertrauensvoll und kompetent.
Das Logo sollte unverwechselbar, einfach und einprägsam sein. Ich könnte mir sehr gut einen Schlüssel vorstellen, da es ja am Ende des gesamten Prozesses stets um eine Schlüsselübergabe geht. Aber da bin ich auch für alles andere offen.
Es wäre schön, wenn das Design in 'Wohlfühlfarben' gehalten ist, nicht so knallig, eher elegant.

```html
<!DOCTYPE html>
<html lang="de">
<head>
<meta charset="utf-8">
<title>Wendholt Immobilien – Visitenkarte</title>
<link rel="stylesheet" href="https://fonts.googleapis.com/css2?family=Quicksand:wght@300;400;500;700&display=swap">
<style>
  :root {
    --page: #e8e5e2;
    --card-light: #a7a5a6;
    --card-dark: #5f5d5e;
    --rose: #b89290;
    --rose-deep: #a5807d;
    --rose-text: #e6cfcc;
    --strip-light: #cbc3c2;
    --detail: #9b9899;
    --white: #f6f4f4;
  }
  * { margin: 0; padding: 0; box-sizing: border-box; }
  html, body {
    width: 1200px; height: 1200px; overflow: hidden;
    background: var(--page);
    font-family: "Quicksand", sans-serif;
  }
  .sheet {
    width: 1200px; height: 1200px;
    display: flex; flex-direction: column;
    align-items: center; justify-content: center; gap: 60px;
  }
  .card {
    position: relative;
    width: 840px; height: 510px;
    border-radius: 4px; overflow: hidden;
    background: radial-gradient(ellipse 75% 80% at 50% 35%, var(--card-light) 0%, #8a8889 45%, var(--card-dark) 100%);
    box-shadow: 0 10px 30px rgba(0,0,0,.18);
  }
  .card__edge {
    position: absolute; left: 0; right: 0; bottom: 0; height: 34px;
  }
  .card__edge::before, .card__edge::after {
    content: ""; position: absolute; left: 0; right: 0;
  }
  .card__edge::before { top: 0; height: 14px; background: var(--strip-light); }
  .card__edge::after { bottom: 0; height: 20px; background: var(--rose-deep); }

  /* front */
  .brand {
    position: absolute; left: 0; right: 0; top: 170px;
    display: flex; align-items: center; justify-content: center; gap: 18px;
    color: var(--white);
  }
  .brand__dot { width: 22px; height: 22px; border-radius: 50%; background: var(--white); }
  .brand__name {
    font-weight: 500; font-size: 46px; letter-spacing: 3px; line-height: 1;
  }
  .front__web {
    position: absolute; left: 0; right: 0; bottom: 62px;
    text-align: center; font-size: 22px; font-weight: 400;
    color: var(--strip-light); letter-spacing: 1px;
  }

  /* back */
  .portrait {
    position: absolute; left: 60px; bottom: 34px;
    width: 340px; height: 420px;
    border-radius: 170px 170px 0 0;
    background: linear-gradient(180deg, #c9b79a 0%, #c8a996 32%, #2f4f93 58%, #1f3d86 100%);
    opacity: .85;
  }
  .nameband {
    position: absolute; left: 420px; right: 0; top: 84px;
    height: 130px; background: var(--rose);
    padding: 22px 0 0 26px; color: var(--rose-text);
  }
  .nameband__name { font-size: 34px; font-weight: 300; line-height: 1.1; color: #f3e6e4; }
  .nameband__name strong { font-weight: 700; }
  .nameband__title { font-size: 21px; font-weight: 400; line-height: 1.25; margin-top: 6px; }
  .contact {
    position: absolute; left: 446px; top: 250px;
    font-size: 21px; line-height: 1.3; color: var(--detail); font-weight: 400;
  }
  .contact__block + .contact__block { margin-top: 20px; }
</style>
</head>
<body>
<main class="sheet">

  <section class="card card--front" aria-label="Visitenkarte Vorderseite">
    <div class="brand">
      <span class="brand__dot"></span>
      <span class="brand__name">WENDHOLT IMMOBILIEN</span>
    </div>
    <p class="front__web">www.wendholt-immobilien.de</p>
    <div class="card__edge"></div>
  </section>

  <section class="card card--back" aria-label="Visitenkarte Rückseite">
    <div class="portrait" role="img" aria-label="Porträtfoto der Maklerin in blauem Oberteil vor grauem Hintergrund"></div>
    <div class="nameband">
      <p class="nameband__name">Larissa <strong>Wendholt</strong></p>
      <p class="nameband__title">Fachmaklerin der<br>Immobilienwirtschaft VIMF</p>
    </div>
    <div class="contact">
      <div class="contact__block">
        <p>Mobil: 0151-24 63 90 7</p>
        <p>info@wendholt-immobilien.de</p>
      </div>
      <div class="contact__block">
        <p>Lindenstieg 14</p>
        <p>48291 Talbrück</p>
      </div>
    </div>
    <div class="card__edge"></div>
  </section>

</main>
</body>
</html>
```